Window Cleaning Leaflet

Hi everyone,

I need a leaflet (couldn't find 'leaflet' as an option when begining this project - so one sided only) to send out to coastal properties in South side Melbourne. The Flyer is aimed at high net individuals, mummies, business people etc who own these properties who don't have time to clean the windows themselves (often multiple levels) and want their home looking fabulous in time for Christmas and NY's celebrations.

I would really love a new and original design for a window washing leaflet. something outside of the norm that 'pops' and makes people feel happy when they look at it.

I guess a point of differentiation is that I'm a female working in a mans industry so appeal to mothers looking for someone who is 'reliable, trustworthy and understanding of peoples needs'.

I have made an outline of what I would like included in the leaflet, so if you could please take a look, feel free to change things around, wording and layout etc. If you can make it sound more professional please do so.

I would like the colours to be 'happy' colours, maybe with a silly season theme?

Overall aesthetically pleasing is a must, I find most window cleaning leaflets fairly mundane and boring, please feel free to think outside the box. The more original the better.

Target Market(s)

People who own large Melbourne homes in affluent suburbs, mainly suburbs with a lot of large coastal properties. Generally owned by high net worth individuals who just don't have tme to clean the windows themselves due to their profession or hectic lifestyles but can afford to pay someone else to do it.

Industry/Entity Type

Window Cleaning

Requirements
Must have
• 1) The name of the business - Tilda’s Glass Gleaming Services
• 2) The coupon special and all details attached:
• Small Homes (up to 12 windows) $120
• Medium Homes (up to 16 windows) $180
• Large Homes (up to 20 windows, 2 storeys) $240
• 20% discount
• *Discount applicable to first time customers only.
• *All services include fly screen, sill and tracks cleaned as well as cobweb removal.
• *Houses with more than 20 windows (or two levels) will have an immediate quote provided upon inspection of the property with 20% discount applied.
• *Tilda’s Glass Gleaming Services are fully insured.
• 3) My contact number - 0418 263 591

```html
<!DOCTYPE html>
<html lang="en">
<head>
<meta charset="utf-8">
<title>Tilda’s Glass Gleaming Services – Leaflet</title>
<link href="https://fonts.googleapis.com/css2?family=Source+Sans+3:ital,wght@0,400;0,600;0,700;1,600;1,700&display=swap" rel="stylesheet">
<style>
  :root{
    --red:#e3262c;
    --red-dark:#a3151a;
    --navy:#1f2a6b;
    --blue:#2b3a97;
    --orange:#f26522;
    --green:#1e8a3e;
    --yellow:#f7e21a;
    --grey-dark:#3b3d42;
    --grey-mid:#8c9099;
    --sky:#8fbfe6;
    --white:#ffffff;
    --text:#222;
  }
  *{margin:0;padding:0;box-sizing:border-box}
  html,body{width:848px;height:1200px;overflow:hidden;background:var(--white)}
  body{font-family:"Source Sans 3",Arial,sans-serif;color:var(--text)}
  .leaflet{position:relative;width:848px;height:1200px;overflow:hidden;background:var(--white)}

  .stripes{position:absolute;left:0;top:0;width:848px;height:62px;display:flex}
  .stripes span{flex:1}

  .window-scene{position:absolute;left:53px;top:80px;width:720px;height:693px;
    background:linear-gradient(90deg,var(--grey-dark) 0%,var(--grey-mid) 30%,var(--sky) 55%,#cfe4f5 75%,var(--grey-dark) 100%);}
  .frame{position:absolute;left:53px;top:80px;width:720px;height:693px;border:14px solid #eceeef;pointer-events:none}

  .ribbon{position:absolute;left:90px;top:10px;width:668px;height:170px}
  .title{position:absolute;left:0;width:848px;top:72px;text-align:center;color:var(--white);
    font-weight:700;font-size:30px;line-height:35px;letter-spacing:.3px}

  .price{position:absolute;left:264px;width:319px;background:var(--white);border:4px solid;border-radius:4px;
    display:flex;align-items:center;padding-left:16px}
  .price .amount{font-size:50px;font-weight:600;line-height:1;display:flex;align-items:flex-start;width:118px}
  .price .amount sup{font-size:22px;margin-top:4px;margin-right:2px}
  .price .tier{font-weight:700;font-size:19px;line-height:1.05}
  .price .tier small{display:block;font-size:15px;font-weight:600}
  .price--small{top:209px;height:58px;border-color:var(--blue);color:var(--blue)}
  .price--medium{top:287px;height:58px;border-color:var(--orange);color:var(--orange)}
  .price--large{top:364px;height:76px;border-color:var(--green);color:var(--green)}

  .promise{position:absolute;left:253px;top:463px;width:340px;height:137px;background:var(--white);
    border:4px solid var(--yellow);border-radius:4px;padding:12px 16px;color:var(--navy);
    font-weight:600;font-size:18.5px;line-height:24px}
  .service-note{position:absolute;right:231px;top:618px;width:200px;text-align:right;color:var(--white);
    font-size:17px;line-height:24px}

  .offer-graphic{position:absolute;left:20px;top:836px;width:370px;height:350px}
  .discount-box{position:absolute;left:143px;top:926px;width:190px;height:200px;background:var(--white);
    border-radius:22px;box-shadow:0 8px 14px rgba(0,0,0,.25);display:flex;flex-direction:column;
    align-items:center;justify-content:center;color:#111;font-weight:700}
  .discount-box .pct{font-size:62px;line-height:1}
  .discount-box .pct sup{font-size:30px}
  .discount-box .off{font-size:36px;letter-spacing:10px;margin-top:4px}

  .cta{position:absolute;left:400px;top:822px;width:440px;font-style:italic;font-weight:600;
    font-size:22px;line-height:27px;color:#111}
  .phone{position:absolute;left:400px;top:874px;font-style:italic;font-weight:700;font-size:33px;color:var(--red)}

  .terms{position:absolute;left:396px;top:942px;width:420px;list-style:none}
  .terms li{position:relative;padding-left:27px;font-size:16px;line-height:20px;margin-bottom:12px;color:#222}
  .terms li svg{position:absolute;left:0;top:2px;width:18px;height:16px}
  .terms strong{color:var(--red)}
</style>
</head>
<body>
<div class="leaflet">

  <div class="stripes" aria-hidden="true">
    <span style="background:#f7e21a"></span><span style="background:#e3262c"></span><span style="background:#2b3a97"></span>
    <span style="background:#f7941d"></span><span style="background:#8dc63f"></span><span style="background:#ec008c"></span>
    <span style="background:#00aeef"></span><span style="background:#fff200"></span><span style="background:#92278f"></span>
    <span style="background:#f26522"></span><span style="background:#39b54a"></span><span style="background:#ed1c24"></span>
    <span style="background:#f9a8c9"></span><span style="background:#2e3192"></span><span style="background:#ffde17"></span>
    <span style="background:#00a99d"></span>
  </div>

  <div class="window-scene" role="img" aria-label="Open white window with a stormy grey sky giving way to clear blue sky and clouds, a red-handled squeegee and white stars"></div>
  <div class="frame" aria-hidden="true"></div>

  <svg class="ribbon" viewBox="0 0 668 170" aria-hidden="true">
    <path d="M0 40 L70 30 L60 80 L80 130 L10 140 L30 90 Z" fill="var(--red-dark)"/>
    <path d="M668 40 L598 30 L608 80 L588 130 L658 140 L638 90 Z" fill="var(--red-dark)"/>
    <path d="M60 20 Q334 60 608 20 L608 130 Q334 170 60 130 Z" fill="var(--red)"/>
  </svg>
  <h1 class="title">TILDA’S GLASS GLEAMING<br>SERVICES</h1>

  <div class="price price--small"><span class="amount"><sup>$</sup>120</span><span class="tier">Small Homes<small>(up to 12 windows)</small></span></div>
  <div class="price price--medium"><span class="amount"><sup>$</sup>180</span><span class="tier">Medium Homes<small>(up to 16 windows)</small></span></div>
  <div class="price price--large"><span class="amount"><sup>$</sup>240</span><span class="tier">Large Homes<small>(up to 20 windows,<br>2 storeys)</small></span></div>

  <p class="promise">Tilda understands and wants to help you enjoy your home looking its best before Christmas and NY’s celebrations begin!</p>

  <p class="service-note">We provide a reliable, professional service, ensuring that your home will sparkle</p>

  <div class="offer-graphic" role="img" aria-label="Colourful paint splash in red, pink, purple, orange and green behind the discount"
       style="background:radial-gradient(circle at 50% 50%,#ec008c 0%,#e3262c 35%,#f7941d 55%,rgba(141,198,63,.6) 68%,rgba(255,255,255,0) 72%)"></div>
  <div class="discount-box"><span class="pct">20<sup>%</sup></span><span class="off">OFF</span></div>

  <p class="cta">Call Tilda today and take advantage of our special introductory offer.</p>
  <p class="phone">Tilda - 0418 263 591</p>

  <ul class="terms">
    <li><svg viewBox="0 0 18 16"><path d="M2 1 L16 6 L2 12 Z" fill="var(--red)"/></svg>Discount applicable to first time customers only.</li>
    <li><svg viewBox="0 0 18 16"><path d="M2 1 L16 6 L2 12 Z" fill="var(--orange)"/></svg>All services include fly screen, sill and tracks cleaned as well as cobweb removal.</li>
    <li><svg viewBox="0 0 18 16"><path d="M2 1 L16 6 L2 12 Z" fill="var(--red)"/></svg>Houses with more than 20 windows (or two levels) will have an immediate quote provided upon inspection of the property with <strong>20% discount</strong> applied.</li>
    <li><svg viewBox="0 0 18 16"><path d="M2 1 L16 6 L2 12 Z" fill="var(--orange)"/></svg>Tilda’s Glass Gleaming Services are fully insured.</li>
  </ul>

</div>
</body>
</html>
```